Plumbing & Heating bussiness card design

i do all plumbing and heating work and need a catchy design. keep it simple but eye catching nothing gimicky
i do 24hr call outs
landlord safety checks
all aspects of plumbing and heating
boiler breakdowns
flue sure reg number 804617
i have put up my old card. not to bothered about the front but i have put up the back for the details. mobile number and office are the same and the email has changed to tolwenpipes@mailvoro.net

Industry/Entity Type

Safety

Contact Information for Business Card

i do 24hr call outs
landlord safety checks
boiler breakdowns

Requirements
Must have
• i do 24hr call outs
• landlord safety checks
• all aspects of plumbing and heating
• boiler breakdowns
• flue sure reg number 804617

```html
<!DOCTYPE html>
<html lang="en">
<head>
<meta charset="utf-8">
<title>R Tolwen Plumbing &amp; Heating – Business Card</title>
<link rel="stylesheet" href="https://fonts.googleapis.com/css2?family=Montserrat:wght@500;700;800&family=Open+Sans:wght@400;600&display=swap">
<style>
  :root {
    --page: #e9e8e6;
    --card-dark: #48494d;
    --card-dark-deep: #3b3c40;
    --card-light: #ffffff;
    --ink: #2b2b2e;
    --muted: #6d6e72;
    --soft: #dcdcdf;
    --blue: #2a9fdc;
    --red: #d12a3c;
    --bullet: #e58a96;
    --badge: #f5d10a;
    --white: #ffffff;
  }
  * { margin: 0; padding: 0; box-sizing: border-box; }
  html, body { width: 1200px; height: 800px; overflow: hidden; }
  body {
    background: var(--page);
    display: flex;
    align-items: center;
    justify-content: center;
    gap: 40px;
    font-family: "Open Sans", sans-serif;
  }

  /* ---------- Back of card (portrait, dark) ---------- */
  .card-back {
    position: relative;
    width: 340px;
    height: 530px;
    border-radius: 22px;
    background: linear-gradient(160deg, var(--card-dark), var(--card-dark-deep));
    overflow: hidden;
    box-shadow: 0 6px 18px rgba(0,0,0,.18);
  }
  .card-back .swooshes { position: absolute; inset: 0; }
  .card-back .brand {
    position: absolute;
    left: 50%;
    top: 50%;
    width: 460px;
    transform: translate(-50%, -50%) rotate(90deg);
    display: flex;
    align-items: center;
    justify-content: center;
    gap: 18px;
  }
  .brand-dot {
    width: 46px; height: 46px;
    border-radius: 50%;
    background: var(--red);
    flex: none;
  }
  .card-back .brand-name {
    font-family: "Montserrat", sans-serif;
    font-weight: 800;
    color: var(--white);
    line-height: 1.05;
    font-size: 38px;
    letter-spacing: .5px;
  }
  .card-back .brand-name span { display: block; font-size: 21px; letter-spacing: 1px; }

  /* ---------- Front of card (landscape, light) ---------- */
  .card-front {
    position: relative;
    width: 700px;
    height: 440px;
    border-radius: 24px;
    background: var(--card-light);
    overflow: hidden;
    box-shadow: 0 6px 18px rgba(0,0,0,.18);
  }
  .card-front .bands { position: absolute; inset: 0; }

  .front-mark {
    position: absolute;
    left: 140px; top: 30px;
    display: flex; align-items: center; gap: 12px;
  }
  .front-mark .brand-dot { background: var(--blue); width: 38px; height: 38px; }
  .front-mark .brand-name {
    font-family: "Montserrat", sans-serif;
    font-weight: 800;
    font-size: 30px;
    color: var(--red);
  }

  .services {
    position: absolute;
    left: 140px; top: 92px;
    list-style: none;
    font-size: 13px;
    line-height: 20px;
    color: var(--muted);
  }
  .services li { position: relative; padding-left: 14px; white-space: nowrap; }
  .services li::before {
    content: "";
    position: absolute; left: 0; top: 7px;
    width: 6px; height: 6px; border-radius: 50%;
    background: var(--bullet);
  }

  .reg-badge {
    position: absolute;
    left: 46px; top: 104px;
    width: 64px; height: 64px;
    background: var(--badge);
    border: 4px solid var(--ink);
  }

  .wordmark {
    position: absolute;
    right: 40px; top: 128px;
    font-family: "Montserrat", sans-serif;
    font-weight: 800;
    color: var(--ink);
    font-size: 40px;
    line-height: 1;
  }
  .wordmark span { display: block; font-size: 21px; letter-spacing: .6px; margin-top: 5px; }

  .contact {
    position: absolute;
    right: 40px; bottom: 24px;
    text-align: right;
    color: var(--white);
  }
  .contact .person {
    font-family: "Montserrat", sans-serif;
    font-weight: 700;
    font-size: 21px;
    line-height: 26px;
    color: var(--blue);
    letter-spacing: 1px;
  }
  .contact .role {
    font-size: 13px;
    font-weight: 600;
    color: var(--soft);
    letter-spacing: 1.5px;
    margin-bottom: 8px;
  }
  .contact .line {
    display: flex; align-items: center; justify-content: flex-end; gap: 8px;
    font-size: 14px; line-height: 22px;
  }
  .icon {
    width: 16px; height: 16px; border-radius: 50%;
    background: var(--blue);
    display: inline-flex; align-items: center; justify-content: center;
  }
  .icon svg { width: 10px; height: 10px; fill: var(--white); }
  .contact .address {
    margin-top: 8px;
    font-family: "Montserrat", sans-serif;
    font-weight: 700;
    font-size: 14px;
    letter-spacing: .5px;
  }
</style>
</head>
<body>

  <section class="card-back" aria-label="Card back">
    <svg class="swooshes" viewBox="0 0 340 530" preserveAspectRatio="none" aria-hidden="true">
      <path d="M70 150 C 110 70, 200 50, 300 80 C 210 70, 130 90, 70 150 Z" fill="var(--blue)"/>
      <path d="M0 390 C 100 410, 200 420, 290 330 C 230 430, 120 450, 0 398 Z" fill="var(--red)"/>
    </svg>
    <div class="brand">
      <div class="brand-dot"></div>
      <div class="brand-name">R TOLWEN<span>PLUMBING &amp; HEATING</span></div>
    </div>
  </section>

  <section class="card-front" aria-label="Card front">
    <svg class="bands" viewBox="0 0 700 440" preserveAspectRatio="none" aria-hidden="true">
      <path d="M0 232 C 180 232, 330 292, 700 236 L700 440 L0 440 Z" fill="var(--card-dark)"/>
      <path d="M0 198 C 120 198, 200 230, 250 262 C 190 226, 110 208, 0 206 Z" fill="var(--blue)"/>
      <path d="M360 262 C 500 286, 620 258, 700 208 L700 236 C 620 282, 500 290, 360 262 Z" fill="var(--red)"/>
    </svg>

    <div class="front-mark">
      <div class="brand-dot"></div>
      <div class="brand-name">R TOLWEN</div>
    </div>

    <div class="reg-badge" role="img" aria-label="Registration badge"></div>

    <ul class="services">
      <li>24hr Call Outs</li>
      <li>Landlord Safety Checks</li>
      <li>All Aspects Of Plumbing And Heating</li>
      <li>Boiler Breakdowns</li>
      <li>Flue Sure Reg Number 804617</li>
    </ul>

    <div class="wordmark">R TOLWEN<span>PLUMBING &amp; HEATING</span></div>

    <div class="contact">
      <div class="person">OWEN MARSH</div>
      <div class="role">DIRECTOR</div>
      <div class="line">07700 900318
        <span class="icon"><svg viewBox="0 0 10 10"><path d="M2 1l2 2-1 1c.5 1.2 1.6 2.3 3 3l1-1 2 2-1.2 1.2C4.5 9 1 5.5.8 2.2z"/></svg></span>
      </div>
      <div class="line">01632 960514
        <span class="icon"><svg viewBox="0 0 10 10"><rect x="1" y="3" width="8" height="5" rx="1"/><rect x="3" y="1.5" width="4" height="2"/></svg></span>
      </div>
      <div class="line">tolwenpipes@mailvoro.net
        <span class="icon"><svg viewBox="0 0 10 10"><path d="M1 2.5h8v5H1z M1 2.5l4 3 4-3" stroke="#2a9fdc" stroke-width=".6"/></svg></span>
      </div>
      <div class="address">14 HARLOW RD, EXFORD, EX9 2QT</div>
    </div>
  </section>

</body>
</html>
```